Business Card Design needed for start up company Pramora

In need of a new business card designed for a start up company based in Sydney, Pramora is a new start up innovative Company, our mission it to make property accessible for everyday Australian and to become the leading Real Estate platform in Australia. We want it to be fresh and clean.

Industry/Entity Type

Financial

Contact Information for Business Card

Section for Name
Section for Title

PRAMORA - Where Doors Open Wide
Mobile:
Direct:

Font styles to use
Sans Serif

Colors
33a6d7
0692cd
0255a3
ffffff

Requirements
Must have
• Logo, all business card details

```html
<!DOCTYPE html>
<html lang="en">
<head>
<meta charset="utf-8">
<title>Pramora – Business Card</title>
<link href="https://fonts.googleapis.com/css2?family=Josefin+Sans:wght@400;600;700&display=swap" rel="stylesheet">
<style>
  :root {
    --sky: #33a6d7;
    --azure: #0692cd;
    --navy: #0255a3;
    --white: #ffffff;
    --ink: #1d1f24;
    --stage: #eceef0;
  }
  * { box-sizing: border-box; margin: 0; padding: 0; }
  html, body {
    width: 1200px; height: 800px; overflow: hidden;
    background: var(--stage);
  }
  .sheet {
    width: 1200px; height: 800px;
    display: flex; flex-direction: column;
    align-items: center; justify-content: center; gap: 40px;
  }
  .card {
    position: relative;
    width: 600px; height: 343px;
    background: var(--white);
    box-shadow: 0 6px 18px rgba(0,0,0,0.10);
    overflow: hidden;
    font-family: "Josefin Sans", sans-serif;
  }

  /* company name, set plainly in the text font */
  .company {
    position: absolute;
    font-weight: 600; color: var(--navy);
    letter-spacing: 0.08em; line-height: 1;
    white-space: nowrap;
  }

  /* front */
  .card--front .company { left: 64px; top: 118px; font-size: 60px; }
  .card--front .band {
    position: absolute; left: 0; right: 0; top: 242px; height: 48px;
    background: linear-gradient(90deg, var(--azure), var(--navy) 55%, var(--azure));
  }

  /* back */
  .card--back .company { left: 60px; top: 160px; font-size: 30px; }
  .rail { position: absolute; left: 310px; top: 0; width: 40px; height: 343px; }

  .contact { position: absolute; left: 370px; top: 74px; }
  .contact__name {
    font-weight: 700; font-size: 19px; letter-spacing: 0.08em;
    color: var(--ink); line-height: 1.1;
  }
  .contact__title {
    font-size: 13px; font-weight: 600; letter-spacing: 0.08em;
    color: var(--azure); text-transform: uppercase; margin-top: 3px;
  }
  .contact__rule { width: 58px; height: 2px; background: var(--azure); margin: 8px 0 9px; }
  .contact__phone {
    font-size: 16px; font-weight: 400; color: #3a3d44;
    letter-spacing: 0.05em; line-height: 1.3; padding-left: 10px;
  }
  .contact__rule--end { margin-left: 20px; }
</style>
</head>
<body>
<main class="sheet">

  <section class="card card--front" aria-label="Card front">
    <p class="company">PRAMORA</p>
    <div class="band" role="img" aria-label="Blue band with faint world map pattern"></div>
  </section>

  <section class="card card--back" aria-label="Card back">
    <p class="company">PRAMORA</p>

    <svg class="rail" viewBox="0 0 40 343" aria-hidden="true">
      <line x1="20" y1="26" x2="20" y2="300" stroke="#0255a3" stroke-width="6" stroke-linecap="round"/>
      <circle cx="20" cy="110" r="16" fill="#ffffff" stroke="#0255a3" stroke-width="2"/>
      <rect x="12" y="102" width="16" height="16" rx="2" fill="#33a6d7"/>
      <circle cx="20" cy="107" r="3" fill="#ffffff"/>
      <path d="M14.5 116 a5.5 5 0 0 1 11 0 z" fill="#ffffff"/>
      <circle cx="20" cy="160" r="16" fill="#ffffff" stroke="#0255a3" stroke-width="2"/>
      <path d="M14 153 l3 -1 2 4 -2 1.5 q1.5 3.5 5 5 l1.5 -2 4 2 -1 3 q-1 1.5 -3 1 q-8 -3 -10.5 -10.5 q-0.5 -2 1 -3z" fill="#0692cd"/>
    </svg>

    <div class="contact">
      <p class="contact__name">DANIEL HART</p>
      <p class="contact__title">General Manager</p>
      <div class="contact__rule"></div>
      <p class="contact__phone">123 456 789</p>
      <p class="contact__phone">123 456 789</p>
      <div class="contact__rule contact__rule--end"></div>
    </div>
  </section>

</main>
</body>
</html>
```